Print on top the name of the company: (Or Similar)
Larkmoor Cleaning & Disinfecting
Because your standards aren't standard.

We adhere to ALL NVB guidelines for both residential and commercial cleaning.

Infection Control is our ultimate goal.

Instructions:
Opening a residential and commercial cleaning and disinfecting company in south Florida.

Targeting high-end residential clients, commercial and healthcare facilities, specializing in Ambulatory Care Guidelines. With a concentration and expertise in targeting Covid 19 and other transmissible pathogens.

UMRE trained.
Owned and operated by a licensed BSN Registered Nurse specially ​trained in Infection Control Prevention with over 25 years experience. Over two decades in Ambulatory Surgery Center Administration, Director of Nursing and Infection Control Prevention ad Consulting.

Looking to create a business flier that emphasizes Cleaning & Disinfection
along with the standard expectation for residential and Commercial cleaning services
Updates

Need extra days to review

Target Market(s)

Residential & Commercial

Font styles to use
Decorative

Requirements
Must have
• A checklist for cleaning services

```html
<!DOCTYPE html>
<html lang="en">
<head>
<meta charset="utf-8">
<title>Larkmoor Cleaning &amp; Disinfecting – Flyer</title>
<link rel="stylesheet" href="https://fonts.googleapis.com/css2?family=Oswald:wght@600;700&family=Montserrat:wght@400;500;700;800&display=swap">
<style>
  :root{
    --navy:#12365c;
    --green:#7cc243;
    --green-mid:#68ad3f;
    --green-deep:#4f9338;
    --green-ring:#2f5e2a;
    --white:#ffffff;
    --ink:#1f2a36;
    --stage:#e4e3ea;
    --photo-light:#e9edf2;
    --photo-mid:#c9d3dc;
  }
  *{box-sizing:border-box;margin:0;padding:0}
  html,body{width:1200px;height:1200px;overflow:hidden;background:var(--stage)}
  .flyer{
    position:absolute;left:148px;top:20px;width:1260px;height:1618px;
    transform:scale(.717);transform-origin:0 0;
    background:var(--white);overflow:hidden;
    font-family:"Montserrat",Arial,sans-serif;color:var(--white);
  }
  .shapes{position:absolute;inset:0}
  .abs{position:absolute}
  .title{left:36px;top:83px;font-family:"Oswald","Arial Narrow",sans-serif;font-weight:700;text-transform:uppercase;white-space:nowrap}
  .title .l1{display:block;font-size:70px;line-height:70px}
  .title .l2{display:block;font-size:98px;line-height:98px}
  .tagline{left:44px;top:256px;font-size:29px;white-space:nowrap}
  .checks{left:52px;top:310px;width:640px;list-style:none;font-size:29px;line-height:36px}
  .checks li{display:flex;gap:14px;margin-bottom:22px}
  .checks svg{flex:none;margin-top:10px}
  .accent{color:var(--green);font-weight:700}
  .viruses{left:300px;top:505px;width:460px;height:260px;border-radius:50%;
    background:radial-gradient(ellipse at center,rgba(226,45,45,.55),rgba(226,45,45,0) 70%)}
  .viruses.soft{left:20px;top:720px;width:640px;height:180px;
    background:radial-gradient(ellipse at center,rgba(185,228,140,.7),rgba(185,228,140,0) 70%)}
  .photo-round{border-radius:50%;border:8px solid var(--white)}
  .photo-a{left:67px;top:540px;width:296px;height:296px;background:linear-gradient(160deg,#9d8c82,#6c625f 60%,#8a7b74)}
  .photo-b{left:388px;top:666px;width:244px;height:244px;background:linear-gradient(150deg,#eef2f6,#c5d1dc 60%,#7a8fb3)}
  .photo-hero{left:546px;top:0;width:714px;height:800px;background:linear-gradient(100deg,var(--photo-mid),var(--photo-light) 45%,#f7f8fa)}
  .opening{left:40px;top:918px;width:480px;font-size:32px;line-height:41px;font-weight:800;color:var(--navy)}
  .trained{left:34px;top:1164px;font-size:27px;font-weight:700;color:var(--navy)}
  .bio{left:34px;top:1207px;width:440px;font-size:19.5px;line-height:24px;color:var(--ink)}
  .brand{left:34px;top:1405px;font-family:"Oswald","Arial Narrow",sans-serif;font-weight:700;font-size:84px;line-height:85px;text-transform:uppercase;color:var(--navy);white-space:nowrap}
  .brand .second{display:block;color:var(--green)}
  .services-tab{left:788px;top:850px;width:472px;height:70px;background:var(--navy);border-radius:35px 0 0 35px;
    font-size:52px;font-weight:800;line-height:70px;padding-left:40px}
  .group-head{right:34px;font-size:36px;font-weight:800}
  .head-commercial{top:960px}
  .head-residential{top:1222px}
  .grid{left:520px;width:720px;display:grid;grid-template-columns:196px 165px 170px 185px;row-gap:30px}
  .grid-commercial{top:1046px}
  .grid-residential{top:1300px;row-gap:40px}
  .item{text-align:right;font-size:23px;line-height:25px;position:relative;padding-right:14px}
  .item::after{content:"";position:absolute;right:0;top:9px;width:9px;height:9px;border-radius:50%;background:var(--navy)}
  .call{right:40px;top:1530px;font-size:19.5px}
  .phone{right:52px;top:1556px;font-size:29px;font-weight:700;display:flex;align-items:center;gap:18px;letter-spacing:.5px}
</style>
</head>
<body>
<main class="flyer">
  <div class="abs photo-hero" role="img" aria-label="Photo of a worker in a white protective suit and respirator wiping a door handle"></div>

  <svg class="shapes" viewBox="0 0 1260 1618" aria-hidden="true">
    <defs>
      <linearGradient id="serviceFill" x1="0" y1="0" x2="0" y2="1">
        <stop offset="0" stop-color="var(--green)"/>
        <stop offset="1" stop-color="var(--green-deep)"/>
      </linearGradient>
    </defs>
    <circle cx="205" cy="490" r="630" fill="var(--navy)"/>
    <ellipse cx="240" cy="900" rx="450" ry="225" fill="var(--green)"/>
    <circle cx="1000" cy="1248" r="520" fill="var(--green-ring)"/>
    <circle cx="1008" cy="1256" r="510" fill="url(#serviceFill)"/>
  </svg>

  <div class="abs viruses soft" role="img" aria-label="Light green virus illustrations"></div>
  <div class="abs viruses" role="img" aria-label="Red virus illustrations"></div>

  <h1 class="abs title"><span class="l1">Larkmoor Cleaning</span><span class="l2">&amp; Disinfecting</span></h1>
  <p class="abs tagline">Because your standards aren't standard.</p>
  <ul class="abs checks">
    <li><svg width="24" height="22" viewBox="0 0 24 22"><rect x="1" y="5" width="16" height="16" fill="none" stroke="#fff" stroke-width="2"/><path d="M5 12l4 4 12-14" fill="none" stroke="#fff" stroke-width="3"/></svg><span>We adhere to ALL NVB guidelines for<br>both residential and commercial<br>cleaning.</span></li>
    <li><svg width="24" height="22" viewBox="0 0 24 22"><rect x="1" y="5" width="16" height="16" fill="none" stroke="#fff" stroke-width="2"/><path d="M5 12l4 4 12-14" fill="none" stroke="#fff" stroke-width="3"/></svg><span><span class="accent">Infection Control</span> is our ultimate goal.</span></li>
  </ul>

  <div class="abs photo-round photo-a" role="img" aria-label="Photo of a worker in protective gear spraying disinfectant outdoors"></div>
  <div class="abs photo-round photo-b" role="img" aria-label="Photo of a gloved hand wiping a door handle"></div>

  <p class="abs opening">Opening a residential and commercial cleaning and disinfecting company in SOUTH FLORIDA.</p>

  <h2 class="abs trained">UMRE trained.</h2>
  <p class="abs bio">Owned and operated by a licensed BSN Registered Nurse specially trained in Infection Control Prevention with over 25 years experience. Over two decades in Ambulatory Surgery Center Administration, Director of Nursing and Infection Control Prevention ad Consulting.</p>

  <div class="abs brand">Larkmoor<span class="second">Cleaning</span></div>

  <h2 class="abs services-tab">Our Services</h2>

  <h3 class="abs group-head head-commercial">Commercial</h3>
  <div class="abs grid grid-commercial">
    <div class="item">Janitorial</div>
    <div class="item">Official</div>
    <div class="item">Floor<br>Maintenance</div>
    <div class="item">Carpet<br>Cleaning</div>
    <div class="item">Construction<br>Clean - Ups</div>
    <div class="item">Move<br>ins</div>
    <div class="item">Move<br>outs</div>
    <div class="item">Estate<br>Celan - Ups</div>
  </div>

  <h3 class="abs group-head head-residential">Residential</h3>
  <div class="abs grid grid-residential">
    <div class="item">House<br>Cleaning</div>
    <div class="item">Before &amp;<br>After Party</div>
    <div class="item">Move<br>ins</div>
    <div class="item">Move<br>Outs</div>
    <div class="item">Holiday<br>Cleaning</div>
    <div class="item">Seasonal<br>Cleaning</div>
    <div class="item">Carpet<br>Cleaning</div>
    <div class="item">Deodorizing<br>&amp; Sanitizing</div>
  </div>

  <p class="abs call">Call us to find out how you can save money this month !</p>
  <p class="abs phone">
    <svg width="26" height="26" viewBox="0 0 26 26" aria-hidden="true"><circle cx="13" cy="13" r="11.5" fill="none" stroke="#fff" stroke-width="2"/><path d="M9 7.5c-1 1-1.2 2.5 0 4.6 1.3 2.3 3 4 5 5.2 2 1.1 3.3.8 4.3-.2l-2.2-2.2-1.5 1c-1.4-.7-2.6-1.9-3.4-3.4l1-1.5z" fill="#fff"/></svg>
    <span>(555) 010 24 68</span>
  </p>
</main>
</body>
</html>
```